Harbor Fresh Cleaning car wrap

I need a car wrap design for my work van that is eye catching and stands out. My type of business is carpet cleaning and tile and grout cleaning along with other services. I would like the services to be listed on the wrap along with the phone number and website.
Also please add that we service Commercial and Residential.
Website is:
HarborFreshCleaning.com
Phone number (555) 203-4619
The services I provide are as follow:
Tile & Grout Cleaning
Carpet Cleaning
Hardwood Floor Cleaning and Refinishing
Upholstery and Rug Cleaning
My business colors consist of blue and white but I am open to using other colors.
My logo is attached in the files.
Commercial and Residential
Carpet Cleaning

```html
<!DOCTYPE html>
<html lang="en">
<head>
<meta charset="utf-8">
<title>Harbor Fresh Cleaning – Van Wrap</title>
<link href="https://fonts.googleapis.com/css2?family=Montserrat:wght@500;600;700;800&display=swap" rel="stylesheet">
<style>
  :root{
    --teal:#128683;
    --teal-mid:#7cc6c1;
    --teal-light:#d5eeec;
    --ink:#2a2e33;
    --white:#ffffff;
    --canvas:#f3f5f5;
    --edge:#dfe5e5;
  }
  *{box-sizing:border-box;margin:0;padding:0}
  html,body{width:1200px;height:800px;overflow:hidden;background:var(--canvas);font-family:"Montserrat",sans-serif;color:var(--ink)}
  .canvas{position:relative;width:1200px;height:800px}

  .wrap-panel{position:absolute;background:var(--white);border:1px solid var(--edge);border-radius:18px;overflow:hidden}
  .wrap-panel--side{left:40px;top:30px;width:1120px;height:380px}
  .wrap-panel--rear{left:320px;top:440px;width:560px;height:330px}

  .wave-band{position:absolute;left:0;right:0;bottom:0;
    background:linear-gradient(to bottom, rgba(255,255,255,0) 0%, var(--teal-light) 30%, var(--teal-mid) 62%, var(--teal) 100%)}
  .wrap-panel--side .wave-band{height:150px}
  .wrap-panel--rear .wave-band{height:110px}
  .door-seam{position:absolute;left:279px;top:0;bottom:0;width:1.5px;background:var(--edge)}

  .brand{position:absolute;text-align:center;z-index:1}
  .brand__name{font-weight:800;color:var(--teal);line-height:1.08;text-transform:uppercase;letter-spacing:.5px}
  .brand__est{display:flex;align-items:center;gap:10px;justify-content:center;font-weight:700;color:var(--teal);margin-top:10px}
  .brand__est::before,.brand__est::after{content:"";height:1px;background:var(--ink);flex:1}

  .contact{position:absolute;text-align:center;z-index:1}
  .contact__phone{font-weight:700;color:var(--teal);white-space:nowrap}
  .contact__web{font-weight:500;color:var(--ink);white-space:nowrap}
  .contact__tag{font-weight:600;color:var(--teal);white-space:nowrap}

  .services{position:absolute;left:0;right:0;display:flex;justify-content:center;align-items:flex-start;z-index:1}
  .service{display:flex;flex-direction:column;align-items:center;text-align:center;font-weight:600;text-transform:uppercase;color:var(--ink);line-height:1.3}
  .service__icon{border:2px solid var(--teal);border-radius:50%;background:var(--white);display:flex;align-items:center;justify-content:center;margin-bottom:8px}
  .service__divider{width:1px;background:var(--ink);opacity:.6;align-self:stretch}

  /* side sizing */
  .wrap-panel--side .brand{left:90px;top:52px;width:480px}
  .wrap-panel--side .brand__name{font-size:42px}
  .wrap-panel--side .brand__est{font-size:12px}
  .wrap-panel--side .contact{left:620px;top:66px;width:440px}
  .wrap-panel--side .contact__phone{font-size:40px}
  .wrap-panel--side .contact__web{font-size:20px;margin-top:6px}
  .wrap-panel--side .contact__tag{font-size:16px;margin-top:10px}
  .wrap-panel--side .services{top:222px;gap:40px}
  .wrap-panel--side .service{font-size:11px;min-width:110px}
  .wrap-panel--side .service__icon{width:46px;height:46px}

  /* rear sizing */
  .wrap-panel--rear .brand{left:20px;top:44px;width:240px}
  .wrap-panel--rear .brand__name{font-size:22px}
  .wrap-panel--rear .brand__est{font-size:9px;margin-top:6px}
  .wrap-panel--rear .contact{left:290px;top:46px;width:250px}
  .wrap-panel--rear .contact__phone{font-size:24px}
  .wrap-panel--rear .contact__web{font-size:13px;margin-top:4px}
  .wrap-panel--rear .contact__tag{font-size:11px;margin-top:8px}
  .wrap-panel--rear .services{top:168px;gap:12px}
  .wrap-panel--rear .service{font-size:8.5px;min-width:100px}
  .wrap-panel--rear .service__icon{width:36px;height:36px;margin-bottom:6px}
</style>
</head>
<body>
<div class="canvas">

  <section class="wrap-panel wrap-panel--side" aria-label="Van side panel">
    <div class="wave-band" role="img" aria-label="Flowing teal wave graphic along the lower body"></div>

    <div class="brand">
      <div class="brand__name">Harbor Fresh Cleaning</div>
      <div class="brand__est">EST. 2010</div>
    </div>

    <div class="contact">
      <div class="contact__phone">(555) 203-4619</div>
      <div class="contact__web">HarborFreshCleaning.com</div>
      <div class="contact__tag">Serving Commercial &amp; Residential</div>
    </div>

    <div class="services">
      <div class="service">
        <span class="service__icon"><svg width="22" height="22" viewBox="0 0 22 22" fill="none" stroke="var(--teal)" stroke-width="1.6"><rect x="2" y="2" width="18" height="18"/><path d="M8 2v18M14 2v18M2 8h18M2 14h18"/></svg></span>
        Tile &amp; Grout<br>Cleaning
      </div>
      <span class="service__divider"></span>
      <div class="service">
        <span class="service__icon"><svg width="24" height="22" viewBox="0 0 24 22" fill="none" stroke="var(--teal)" stroke-width="1.6"><circle cx="7" cy="11" r="5"/><circle cx="7" cy="11" r="2"/><path d="M7 16h15l-3-10H7"/></svg></span>
        Carpet<br>Cleaning
      </div>
      <span class="service__divider"></span>
      <div class="service">
        <span class="service__icon"><svg width="22" height="22" viewBox="0 0 22 22" fill="none" stroke="var(--teal)" stroke-width="1.6"><rect x="2" y="2" width="18" height="18"/><path d="M8 2v18M14 2v18M2 10h6M14 13h6M8 6h6"/></svg></span>
        Hardwood Floor<br>Cleaning &amp; Refinishing
      </div>
      <span class="service__divider"></span>
      <div class="service">
        <span class="service__icon"><svg width="24" height="22" viewBox="0 0 24 22" fill="none" stroke="var(--teal)" stroke-width="1.6"><path d="M6 10V5a2 2 0 0 1 2-2h8a2 2 0 0 1 2 2v5"/><rect x="2" y="9" width="4" height="7" rx="1"/><rect x="18" y="9" width="4" height="7" rx="1"/><path d="M6 13h12M4 16v3M20 16v3"/></svg></span>
        Upholstery &amp;<br>Rug Cleaning
      </div>
    </div>
  </section>

  <section class="wrap-panel wrap-panel--rear" aria-label="Van rear doors">
    <div class="wave-band" role="img" aria-label="Flowing teal wave graphic across the lower doors"></div>
    <span class="door-seam"></span>

    <div class="brand">
      <div class="brand__name">Harbor Fresh Cleaning</div>
      <div class="brand__est">EST. 2010</div>
    </div>

    <div class="contact">
      <div class="contact__phone">(555) 203-4619</div>
      <div class="contact__web">HarborFreshCleaning.com</div>
      <div class="contact__tag">Serving Commercial &amp; Residential</div>
    </div>

    <div class="services">
      <div class="service">
        <span class="service__icon"><svg width="18" height="18" viewBox="0 0 22 22" fill="none" stroke="var(--teal)" stroke-width="1.8"><rect x="2" y="2" width="18" height="18"/><path d="M8 2v18M14 2v18M2 8h18M2 14h18"/></svg></span>
        Tile &amp; Grout<br>Cleaning
      </div>
      <span class="service__divider"></span>
      <div class="service">
        <span class="service__icon"><svg width="20" height="18" viewBox="0 0 24 22" fill="none" stroke="var(--teal)" stroke-width="1.8"><circle cx="7" cy="11" r="5"/><circle cx="7" cy="11" r="2"/><path d="M7 16h15l-3-10H7"/></svg></span>
        Carpet<br>Cleaning
      </div>
      <span class="service__divider"></span>
      <div class="service">
        <span class="service__icon"><svg width="18" height="18" viewBox="0 0 22 22" fill="none" stroke="var(--teal)" stroke-width="1.8"><rect x="2" y="2" width="18" height="18"/><path d="M8 2v18M14 2v18M2 10h6M14 13h6M8 6h6"/></svg></span>
        Hardwood Floor<br>Cleaning &amp; Refinishing
      </div>
      <span class="service__divider"></span>
      <div class="service">
        <span class="service__icon"><svg width="20" height="18" viewBox="0 0 24 22" fill="none" stroke="var(--teal)" stroke-width="1.8"><path d="M6 10V5a2 2 0 0 1 2-2h8a2 2 0 0 1 2 2v5"/><rect x="2" y="9" width="4" height="7" rx="1"/><rect x="18" y="9" width="4" height="7" rx="1"/><path d="M6 13h12M4 16v3M20 16v3"/></svg></span>
        Upholstery &amp;<br>Rug Cleaning
      </div>
    </div>
  </section>

</div>
</body>
</html>
```